Purchase Protection Subscription Program needs a refreshed website

We are refreshing an existing website www.carevaultplus.example. This is a purchase protection product which allows its members to receive extended warranty on the items they buy, receive a rebate of 50% on a repair of an item, a personal shopping concierge, etc. We are looking for a fresh, clean approach - with mass appeal to both men and woman. The site should convey trust, and ease of use.

Thanks to everyone who posted designs. Amazing work! It was a very difficult decision!

```html
<!DOCTYPE html>
<html lang="en">
<head>
<meta charset="utf-8">
<title>CareVault Plus — Purchase Protection</title>
<link rel="stylesheet" href="https://fonts.googleapis.com/css2?family=Oswald:wght@400;500&family=Open+Sans:ital,wght@0,400;0,600;0,700;1,400&display=swap">
<style>
:root{
  --brown:#6b4a0c;
  --red:#8c0c05;
  --orange:#f07f1e;
  --accent:#f07f1e;
  --text:#5a5a5a;
  --heading:#5e5e5e;
  --footer-red:#8c1a10;
  --white:#fff;
}
*{box-sizing:border-box;margin:0;padding:0}
html,body{width:835px;height:1200px;overflow:hidden;background:var(--white)}
body{position:relative;font-family:"Open Sans",sans-serif;color:var(--text)}
.abs{position:absolute}

/* header */
.site-header{left:0;top:0;width:835px;height:47px;border-top:2px solid var(--red);background:var(--white)}
.brand{left:115px;top:13px;font-size:16px;color:#333;white-space:nowrap}
.nav-link{top:16px;font-size:10px;color:#333;text-decoration:none;white-space:nowrap;line-height:14px}
.nav-link.current{color:var(--accent)}
.nav-underline{left:293px;top:33px;width:37px;height:2px;background:var(--accent)}
.btn-profile{left:552px;top:12px;width:116px;height:23px;background:#ececec;border-radius:3px;font-size:8.5px;font-weight:700;color:#555;display:flex;align-items:center;justify-content:center;letter-spacing:.3px;white-space:nowrap}
.btn-login{left:674px;top:12px;width:42px;height:23px;background:#a3241c;border-radius:3px;font-size:8.5px;font-weight:700;color:#fff;display:flex;align-items:center;justify-content:center}

/* hero */
.hero-photo{left:0;top:47px;width:835px;height:356px;background:linear-gradient(90deg,#cfd8b0 0%,#a9c17a 25%,#c9d0a7 45%,#c79b79 62%,#a8765b 78%,#d9dde6 100%)}

/* feature cards */
.card-frame{width:197px;height:222px;background:#f1f1f1}
.card{width:189px;height:214px;color:#fff;padding:0 12px 0 17px}
.card.brown{background:var(--brown)}
.card.red{background:var(--red)}
.card.orange{background:var(--orange)}
.card-icon{width:68px;height:68px;border-radius:50%;background:#fff;display:flex;align-items:center;justify-content:center}
.card-title{font-family:"Oswald",sans-serif;font-weight:400;font-size:22px;line-height:1;margin-top:46px;text-transform:uppercase}
.card-sub{font-family:"Oswald",sans-serif;font-size:12.5px;line-height:1.1;text-transform:uppercase;margin-bottom:8px}
.card p{font-size:8.9px;line-height:14.2px}
.card .plus{font-size:12px;font-weight:600;line-height:1.2;margin-bottom:2px}
.card ul{list-style:none;margin-top:7px;font-size:8.9px;line-height:14.2px}
.card li{padding-left:18px;position:relative}
.card li::before{content:"";position:absolute;left:3px;top:3px;width:4px;height:7px;border:solid #fff;border-width:0 2px 2px 0;transform:rotate(45deg)}
.learn-more{left:17px;top:178px;width:87px;height:24px;background:#fff;border-radius:2px;box-shadow:0 2px 2px rgba(0,0,0,.25);font-size:9.5px;font-weight:700;color:#4a3a1a;display:flex;align-items:center;justify-content:center}

/* section headings */
.section-heading{font-family:"Oswald",sans-serif;font-weight:400;font-size:18px;color:var(--heading);display:flex;align-items:center;gap:8px;width:602px;left:115px;white-space:nowrap}
.section-heading::after{content:"";flex:1;height:6px;background:repeating-linear-gradient(45deg,#e4e4e4 0 1px,#f2f2f2 1px 3px);margin-top:3px}
.welcome-text{left:115px;top:569px;width:604px;font-size:8.8px;line-height:14.2px;text-align:justify}

/* how it works */
.how-band{left:0;top:640px;width:835px;height:307px;background:#f7f7f7}
.step-icon{width:76px;height:76px;border-radius:50%;background:var(--brown);display:flex;align-items:center;justify-content:center}
.step-num{width:32px;height:32px;border-radius:50%;background:#e3e3e3;border:2px solid #f7f7f7;font-size:16px;font-weight:700;color:#5a4316;display:flex;align-items:center;justify-content:center}
.step-title{font-size:11.5px;font-weight:700;color:var(--brown);text-align:center;line-height:14px}
.step-body{font-size:8.9px;line-height:14.2px;color:#555;text-align:justify}
.step-list{list-style:none;font-size:7.8px;line-height:10.5px;color:#555;margin-top:8px}
.step-list li{position:relative;padding-left:15px;margin-bottom:4px;text-align:justify}
.step-list li::before{content:"";position:absolute;left:3px;top:0;width:4px;height:7px;border:solid var(--brown);border-width:0 2px 2px 0;transform:rotate(45deg)}

.disclaimer{left:128px;top:969px;width:570px;font-size:7.6px;line-height:14.2px;font-style:italic;color:#777;text-align:justify}

/* footer */
.site-footer{left:0;top:1060px;width:835px;height:140px;background:#f3f3f3;border-top:1px solid #e8e8e8}
.footer-heading{font-family:"Oswald",sans-serif;font-size:10.5px;font-weight:400;color:var(--footer-red);text-transform:uppercase}
.footer-links{list-style:none;font-size:8.8px;line-height:14.2px;color:#555;white-space:nowrap}
.divider{width:1px;height:108px;background:#dcdcdc}
.social li{display:flex;align-items:center;gap:8px;margin-bottom:5.5px}
.social .dot{width:12px;height:12px;border:1px solid #777;border-radius:50%}
.contact li{display:flex;gap:8px;margin-bottom:3px;line-height:12px}
.contact svg{flex:none;margin-top:1px}
.footer-brand{left:507px;top:1084px;font-size:16px;color:#333}
.copyright{left:508px;top:1112px;font-size:8.8px;line-height:14.2px;color:#555}
</style>
</head>
<body>

<header class="site-header abs">
  <div class="brand abs">CareVault Plus</div>
  <a class="nav-link current abs" href="#" style="left:298px">Home</a>
  <a class="nav-link abs" href="#" style="left:338px">About Us</a>
  <a class="nav-link abs" href="#" style="left:390px">Product Features</a>
  <a class="nav-link abs" href="#" style="left:476px">Contact Us</a>
  <div class="nav-underline abs"></div>
  <div class="btn-profile abs">MANAGE USER PROFILE</div>
  <div class="btn-login abs">LOGIN</div>
</header>

<div class="hero-photo abs" role="img" aria-label="Smiling couple embracing outdoors in warm sunlight with green foliage behind"></div>

<div class="card-frame abs" style="left:116px;top:300px"></div>
<div class="card-frame abs" style="left:321px;top:300px"></div>
<div class="card-frame abs" style="left:527px;top:300px"></div>

<section class="card brown abs" style="left:116px;top:300px">
  <h2 class="card-title">Valuable</h2>
  <div class="card-sub">Purchase Protection</div>
  <p style="font-weight:600">Get 5 unique ways to get more out of the things you buy:</p>
  <ul><li>Warranty extension</li><li>Repair bill rebate</li><li>Product return guarantee</li></ul>
  <div class="learn-more abs">LEARN MORE</div>
</section>
<section class="card red abs" style="left:321px;top:300px">
  <h2 class="card-title">Easy</h2>
  <div class="card-sub">Claims Process</div>
  <p style="text-align:justify">Using CareVault Plus has never been easier. Just send us copies, scans or photos of your receipts — we'll store them securely online. Then download what you need and submit your claim online.</p>
  <div class="learn-more abs">LEARN MORE</div>
</section>
<section class="card orange abs" style="left:527px;top:300px">
  <h2 class="card-title">One Low</h2>
  <div class="card-sub">Monthly Fee</div>
  <div class="plus">Plus</div>
  <p style="text-align:justify">Get a $5 bonus rebate each calender quarter to use on home electronics &amp; appliance purchases!</p>
  <div class="learn-more abs">LEARN MORE</div>
</section>

<div class="card-icon abs" style="left:176px;top:267px">
  <svg width="34" height="34" viewBox="0 0 34 34"><path d="M17 4 L28 8 V17 C28 24 23 28 17 31 C11 28 6 24 6 17 V8 Z" fill="none" stroke="#6b4a0c" stroke-width="3"/><path d="M12 17 L16 21 L23 13" fill="none" stroke="#6b4a0c" stroke-width="3"/></svg>
</div>
<div class="card-icon abs" style="left:382px;top:267px">
  <svg width="30" height="34" viewBox="0 0 30 34"><rect x="4" y="2" width="22" height="30" rx="2" fill="none" stroke="#8c0c05" stroke-width="2.5"/><circle cx="11" cy="10" r="3" fill="#8c0c05"/><path d="M16 9h7M16 13h7M8 19h15M8 23h15M8 27h10" stroke="#8c0c05" stroke-width="2"/></svg>
</div>
<div class="card-icon abs" style="left:588px;top:267px">
  <svg width="36" height="30" viewBox="0 0 36 30"><rect x="3" y="6" width="30" height="18" rx="2" transform="rotate(-15 18 15)" fill="#f07f1e"/><circle cx="18" cy="15" r="5" fill="#fff"/></svg>
</div>

<h2 class="section-heading abs" style="top:535px">Wlecome to CareVault Plus</h2>
<p class="welcome-text abs">CVP helps people cope with the complexities of modern life. We provide our customers with support and protection for what's really important to them, including their credit cards, personal information and identities. When these are lost, damaged or stolen we know that our customers need help to make things right. And that's precisely what we do. We deliver immediate repair or restoration through cost-effective and straight-forward assistance that lets our customers to continue with life -- without a worry. We call this life assistance.</p>

<div class="how-band abs"></div>
<h2 class="section-heading abs" style="top:646px">How it Works</h2>

<div class="step-icon abs" style="left:168px;top:684px">
  <svg width="34" height="30" viewBox="0 0 34 30"><path d="M3 12h28l-3 15H6z" fill="#fff"/><path d="M10 12l7-9 7 9" fill="none" stroke="#fff" stroke-width="3"/><path d="M12 16v8M17 16v8M22 16v8" stroke="#6b4a0c" stroke-width="2"/></svg>
</div>
<div class="step-icon abs" style="left:382px;top:684px">
  <svg width="26" height="32" viewBox="0 0 26 32"><path d="M9 2h15v28H2V9z" fill="#fff"/><path d="M2 9h7V2z" fill="#6b4a0c"/></svg>
</div>
<div class="step-icon abs" style="left:594px;top:684px">
  <svg width="28" height="34" viewBox="0 0 30 34"><rect x="4" y="2" width="22" height="30" rx="2" fill="none" stroke="#fff" stroke-width="2.5"/><circle cx="11" cy="10" r="3" fill="#fff"/><path d="M16 9h7M16 13h7M8 19h15M8 23h15M8 27h10" stroke="#fff" stroke-width="2"/></svg>
</div>
<div class="step-num abs" style="left:161px;top:727px">1</div>
<div class="step-num abs" style="left:375px;top:727px">2</div>
<div class="step-num abs" style="left:586px;top:727px">3</div>

<div class="abs" style="left:117px;top:771px;width:172px">
  <h3 class="step-title">Make your purchases</h3>
  <p class="step-body" style="text-align:center;margin-top:3px">Shop like you normally do — except now, you don't need to worry about things like...</p>
  <ul class="step-list">
    <li>Your warranty running out too soon</li>
    <li>Older household appliances that are expensive to repair</li>
    <li>Returning something outside of the store's return policy</li>
    <li>Whether you're getting the best deal on an item</li>
    <li>The cost of restocking big-ticket returns</li>
  </ul>
</div>
<div class="abs" style="left:331px;top:771px;width:170px">
  <h3 class="step-title">Store your receipts</h3>
  <p class="step-body" style="margin-top:3px">Send us a copy, scan, or photo of your receipts and other purchase documents via regular mail, email, mobile phone or our smartphone app — up to 10 per month. We'll scan the documents, extract and verify the data, then categorize and organize them online in your secure account.</p>
</div>
<div class="abs" style="left:544px;top:771px;width:169px">
  <h3 class="step-title">Submit your claims</h3>
  <p class="step-body" style="margin-top:3px">For most claims, simply log into our secure website and submit your information online. You'll already have all of your receipts at your fingertips, organized and ready to attach to your claim. And once your eligible claim is verified and approved, we'll send reimbursement by check in 4-6 weeks.</p>
</div>

<p class="disclaimer abs">*Exclusions and limitations apply. See Terms and Conditions for complete product benefit details. Warranty Extension and Repair Bill Rebate benefits are not available in Maine. Warranty Extension and Repair Bill Rebate benefits are provided by Northfield Product Care Group, except in Arizona, Florida, Oklahoma and Wisconsin, where they are provided by Warranty Relay, Incorporated (FL License Number 24518), both of which are located at 410 Harbor Row, Lakeview, IL 60000, (555) 010-3000. The programs are administered by Brightline Program Services, Inc., 410 Harbor Row, Lakeview, IL 60000, (555) 010-3000. Bonus Rebates are limited to one rebate per purchased item and one purchase per calendar quarter.</p>

<footer class="site-footer abs"></footer>
<div class="abs" style="left:117px;top:1078px">
  <h4 class="footer-heading">Who We Are</h4>
  <ul class="footer-links" style="margin-top:8px">
    <li>Home</li><li>About Us</li><li>Contact Us</li><li>Privacy</li><li>Product Features</li><li>How It Works</li>
  </ul>
</div>
<div class="divider abs" style="left:212px;top:1080px"></div>
<div class="abs" style="left:230px;top:1078px">
  <h4 class="footer-heading">Follow Us</h4>
  <ul class="footer-links social" style="margin-top:8px">
    <li><span class="dot"></span>Social Page</li>
    <li><span class="dot"></span>Updates</li>
    <li><span class="dot"></span>Network</li>
  </ul>
</div>
<div class="divider abs" style="left:315px;top:1080px"></div>
<div class="abs" style="left:339px;top:1078px">
  <h4 class="footer-heading">Contact Info</h4>
  <ul class="footer-links contact" style="margin-top:8px">
    <li><svg width="9" height="11" viewBox="0 0 9 11"><path d="M4.5 0A4 4 0 0 0 .5 4c0 3 4 7 4 7s4-4 4-7a4 4 0 0 0-4-4z" fill="#666"/><circle cx="4.5" cy="4" r="1.5" fill="#f3f3f3"/></svg><span>P.O. Box 1200 Fairhaven,<br>MN 55000</span></li>
    <li><svg width="9" height="10" viewBox="0 0 9 10"><path d="M1 1l2-1 1.5 3-1 1c.5 1.5 1.5 2.5 3 3l1-1 1.5 1.5-1 2C4 9 0 5 1 1z" fill="#666"/></svg><span>(555) 014-8052</span></li>
    <li><svg width="10" height="8" viewBox="0 0 10 8"><rect width="10" height="8" fill="#666"/><path d="M0 0l5 4 5-4" fill="none" stroke="#f3f3f3"/></svg><span>info@carevaultplus.example</span></li>
  </ul>
</div>
<div class="divider abs" style="left:483px;top:1080px"></div>
<div class="footer-brand abs">CareVault Plus</div>
<p class="copyright abs">Copyright © 2014 www.carevaultplus.example.<br>All rights reserved.</p>

</body>
</html>
```